The Hollowmere Stillhouse - Gin Bottle Label

Hi Designers,

We are currently looking for some fresh ideas regarding a label for our gin bottle. We are relatively small and with an emphasis on a quality tipple
made from the very finest and responsibly sourced botanicals. Our operation concentrates on small batch/hand crafted in its purest sense and we would like to reflect this in our brand.
We are looking for a label to read The Hollowmere Stillhouse and have feminine accents with a primary background colour similar to Wrenfield green/blue. Things like Sakura branches with blossom, floral, pretty scrolling perhaps around either full or partial boarder. Gold foil might be used to accent the black border/highlight the word "Hollowmere" and perhaps any floral pattern.
There could reconsideration given to include two boxes "Batch No" and "Bottle No" which would remain empty and filled out by hand during bottling.
Our gin will be 45%ABV
Some floral designs might look good as though they were watercolours in appearance perhaps.
Our bottles are clear medicine style of which I shall attatch a pic.
We are pretty excited about this and would invite anyone with flair and great ideas to have fun with this design.

With kind regards,

Max

Target Market(s)

People who adore bespoke Gin and would be predominately female.

Colors
86cfc6

Requirements
Must have
• We love the Wrenfield green tones and this well may be our label colour with your design.
• The Hollowmere Stillhouse - Gin - 45ABV
Nice to have
• Batch No & Bottle No boxes

```html
<!DOCTYPE html>
<html lang="en">
<head>
<meta charset="utf-8">
<title>The Hollowmere Stillhouse – Gin Label</title>
<link href="https://fonts.googleapis.com/css2?family=Montserrat:wght@400;500;600;700&family=Josefin+Sans:wght@700&display=swap" rel="stylesheet">
<style>
  :root {
    --label-teal: #8acdc5;
    --panel-mint: #b9e0da;
    --ink: #1f1f1f;
    --ink-soft: #3b3b3b;
    --ornament-tone: #4f6f6b;
    --page-bg: #ffffff;
  }
  html, body {
    margin: 0;
    padding: 0;
    width: 1200px;
    height: 1000px;
    overflow: hidden;
    background: var(--page-bg);
    font-family: "Montserrat", Arial, sans-serif;
  }
  .canvas {
    position: relative;
    width: 1200px;
    height: 1000px;
  }
  .label {
    position: absolute;
    left: 310px;
    top: 190px;
    width: 580px;
    height: 620px;
    background: var(--label-teal);
  }
  .label-frame {
    position: absolute;
    left: 30px;
    top: 31px;
    width: 519px;
    height: 558px;
    box-sizing: border-box;
    border: 2px solid var(--ink);
    display: grid;
    grid-template-rows: 156px 284px 58px 1fr;
  }
  .brand-block {
    border-bottom: 2px solid var(--ink);
    display: flex;
    flex-direction: column;
    align-items: center;
    justify-content: center;
    color: var(--ink);
    text-transform: uppercase;
  }
  .brand-article {
    font-weight: 600;
    font-size: 18px;
    letter-spacing: 6px;
    margin-right: -6px;
  }
  .brand-name {
    font-weight: 700;
    font-size: 40px;
    letter-spacing: 3px;
    margin: 6px -3px 4px 0;
    line-height: 1;
  }
  .brand-descriptor {
    font-weight: 600;
    font-size: 18px;
    letter-spacing: 5px;
    margin-right: -5px;
  }
  .product-block {
    background: var(--panel-mint);
    border-bottom: 2px solid var(--ink);
    position: relative;
    text-align: center;
  }
  .tagline {
    margin: 34px 0 0;
    font-weight: 500;
    font-size: 20.5px;
    line-height: 33px;
    letter-spacing: 2px;
    color: var(--ink-soft);
    text-transform: uppercase;
  }
  .product-name {
    position: absolute;
    left: 0;
    right: 0;
    top: 150px;
    margin: 0;
    font-family: "Josefin Sans", "Montserrat", sans-serif;
    font-weight: 700;
    font-size: 104px;
    line-height: 1;
    letter-spacing: 2px;
    color: var(--ink);
  }
  .ornament {
    position: absolute;
    top: 158px;
    width: 102px;
    height: 88px;
    border-radius: 40px;
    background: radial-gradient(circle at 50% 50%, var(--ornament-tone), rgba(79,111,107,0.35));
  }
  .ornament--left { left: 26px; }
  .ornament--right { right: 28px; }
  .details-row {
    border-bottom: 2px solid var(--ink);
    display: grid;
    grid-template-columns: 125px 1fr;
    align-items: stretch;
    color: var(--ink);
  }
  .volume {
    border-right: 2px solid var(--ink);
    display: flex;
    align-items: center;
    justify-content: center;
    font-weight: 700;
    font-size: 23px;
    letter-spacing: 2px;
  }
  .fill-fields {
    display: flex;
    align-items: center;
    padding-left: 12px;
    gap: 96px;
    font-weight: 500;
    font-size: 19px;
  }
  .origin-row {
    display: grid;
    grid-template-columns: 385px 1fr;
    color: var(--ink-soft);
  }
  .origin {
    border-right: 2px solid var(--ink);
    display: flex;
    align-items: center;
    justify-content: center;
    font-weight: 400;
    font-size: 22px;
    letter-spacing: 3px;
    text-transform: uppercase;
  }
  .strength {
    display: flex;
    align-items: center;
    justify-content: center;
    font-weight: 700;
    font-size: 22px;
    color: var(--ink-soft);
  }
</style>
</head>
<body>
  <main class="canvas">
    <section class="label" aria-label="Gin bottle label">
      <div class="label-frame">
        <header class="brand-block">
          <span class="brand-article">The</span>
          <span class="brand-name">Hollowmere</span>
          <span class="brand-descriptor">Stillhouse</span>
        </header>

        <div class="product-block">
          <p class="tagline">The Finest<br>Small Batch Hand Crafted<br>London Dry</p>
          <div class="ornament ornament--left" role="img" aria-label="Black floral scroll ornament with leaves"></div>
          <h1 class="product-name">GIN</h1>
          <div class="ornament ornament--right" role="img" aria-label="Black floral scroll ornament with leaves"></div>
        </div>

        <div class="details-row">
          <div class="volume">70cl&nbsp;℮</div>
          <div class="fill-fields">
            <span class="batch-field">Batch №</span>
            <span class="bottle-field">Bottle №</span>
          </div>
        </div>

        <footer class="origin-row">
          <div class="origin">Distilled in England</div>
          <div class="strength">45%ABV</div>
        </footer>
      </div>
    </section>
  </main>
</body>
</html>
```